Web-Design for Electrcian Company

Our Customer is a small business electrian in Switzerland. He is looking for a fresh and innovative website design. He is well known for his extra service, and that they always go for the extra-mile! In his logo you also see that positive and fresh image the try to bring to the customer. the main colors are black, red and white.

the website structure will be:

- home
- services (with submenu for each service)
- references (with submenu for each category of services)
- about us (2 submenus: history and staff)
- links
- Contact

Target Market(s)

Architects, building owners, people from the age of 35 up...

Industry/Entity Type

Small Business

```html
<!DOCTYPE html>
<html lang="en">
<head>
<meta charset="utf-8">
<title>Brunner + Team Elektro AG</title>
<link href="https://fonts.googleapis.com/css2?family=Oswald:wght@400;500&family=PT+Sans:wght@400;700&family=PT+Sans+Narrow:wght@400;700&family=Noto+Serif&family=Open+Sans:ital,wght@0,400;0,600;1,400&family=Montserrat:wght@400;600&display=swap" rel="stylesheet">
<style>
:root{
  --red:#c8251a;
  --red-dark:#a8200f;
  --hero-top:#e98c72;
  --hero-bottom:#b4230d;
  --ink:#2b2b2b;
  --grey:#555;
  --light:#8c8c8c;
  --rule:#e4e4e4;
  --white:#fff;
}
*{box-sizing:border-box;margin:0;padding:0}
html,body{width:1039px;height:1200px;overflow:hidden;background:var(--white)}
body{position:relative;font-family:"Open Sans",sans-serif;color:var(--ink)}
.abs{position:absolute}

.brand{left:123px;top:40px;font-family:"PT Sans",sans-serif;font-size:20px;color:#1a1a1a;display:flex;align-items:center;gap:14px}
.brand b{font-weight:700}
.brand .dot{width:58px;height:58px;border-radius:50%;border:3px solid var(--red)}
.nav{left:455px;top:46px;display:flex;gap:13px;font-family:"PT Sans",sans-serif;font-size:15px;color:#333}
.nav a{color:inherit;text-decoration:none;display:flex;align-items:center;gap:5px}
.nav a::before{content:"";width:10px;height:10px;border-radius:50%;background:#8a8a8a}
.nav a.active span{border-bottom:2px solid var(--red);padding-bottom:1px}

.hero{left:0;top:108px;width:1039px;height:297px;background:linear-gradient(180deg,var(--hero-top),#d8613f 55%,var(--hero-bottom))}
.hero-photo{left:123px;top:108px;width:303px;height:297px;background:linear-gradient(160deg,#f3c9b0,#c98468 55%,#5a2b22)}
.hero-title{left:441px;top:135px;font-family:"Montserrat",sans-serif;font-size:32px;color:#2a1a16;letter-spacing:.5px}
.hero-title b{font-weight:600}
.hero-tag{left:441px;top:175px;font-family:"Noto Serif",serif;font-size:28px;color:#3a1c14;letter-spacing:.6px}
.hero-text{left:443px;top:224px;width:474px;font-size:11.6px;line-height:22px;color:#3a2018;text-align:justify}
.cta{left:443px;top:327px;width:159px;height:39px;border-radius:4px;background:linear-gradient(#555,#2a2a2a);border:1px solid #1c1c1c;color:#fff;font-family:"Oswald",sans-serif;font-size:19px;display:flex;align-items:center;justify-content:center;gap:12px;box-shadow:0 2px 3px rgba(0,0,0,.35)}
.cta svg{width:9px;height:10px}
.dots{left:878px;top:375px;display:flex;gap:5px}
.dots i{width:10px;height:10px;border-radius:50%;background:#fff}
.dots i.on{background:#1a1a1a}

.section-title{left:122px;top:424px;font-family:"Oswald",sans-serif;font-size:29px;color:#3b3b3b;letter-spacing:.2px;transform:scaleX(.88);transform-origin:left}
.service{width:253px}
.service .thumb{height:164px;border:1px solid #bbb}
.service p{margin-top:10px;font-family:"PT Sans",sans-serif;font-size:15px;color:#3a3a3a;padding-left:1px}

.divider{left:121px;top:912px;width:796px;height:3px;background:var(--rule)}
.col-title{top:937px;font-family:"Oswald",sans-serif;font-size:24px;color:#3b3b3b;transform:scaleX(.88);transform-origin:left}
.news{left:121px;top:980px;width:238px}
.news h4{font-family:"Oswald",sans-serif;font-weight:400;font-size:14px;color:var(--red);margin-bottom:6px}
.news p{font-size:9.2px;line-height:17px;color:var(--light);text-align:justify;margin-bottom:13px}
.quote{left:393px;top:979px;width:237px;font-style:italic;font-size:9.2px;line-height:17px;color:var(--light);text-align:justify}
.quote .who{margin-top:7px;font-weight:600;color:#555}
.quote a{color:var(--red);display:block;line-height:14px}
.team{left:663px;top:977px;display:grid;grid-template-columns:repeat(3,77px);gap:20px 11px}
.team div{height:67px;border:2px solid #fff;box-shadow:0 1px 3px rgba(0,0,0,.4);background:linear-gradient(#d9b8a3,#a67c66)}

.footer{left:0;top:1149px;width:1039px;height:51px;background:linear-gradient(var(--red),var(--red-dark));color:#fff;font-family:"PT Sans Narrow",sans-serif;font-size:16px}
.footer .line{position:absolute;left:123px;top:14px;letter-spacing:.3px}
.footer .line b{font-family:"PT Sans",sans-serif;font-weight:700}
.footer .line .nm{font-family:"PT Sans",sans-serif}
.social{position:absolute;top:15px;width:20px;height:20px;border-radius:3px;background:#6f97c7}
</style>
</head>
<body>
<header>
  <div class="abs brand"><span><b>Brunner + Team</b> Elektro AG</span><span class="dot"></span></div>
  <nav class="abs nav">
    <a class="active" href="#"><span>Home</span></a>
    <a href="#"><span>Services</span></a>
    <a href="#"><span>Refrences</span></a>
    <a href="#"><span>About Us</span></a>
    <a href="#"><span>Links</span></a>
    <a href="#"><span>Contacts</span></a>
  </nav>
</header>

<section>
  <div class="abs hero"></div>
  <div class="abs hero-photo" role="img" aria-label="Portrait of a smiling company representative"></div>
  <h1 class="abs hero-title"><b>Brunner + Team</b> Elektro AG</h1>
  <h2 class="abs hero-tag">Complete Electrical Solutions</h2>
  <p class="abs hero-text">Lorem Ipsum is simply dummy text of the printing and typesetting industry. Lorem Ipsum has been the industry's standard dummy text ever since the 1500s, when an unknown printer took a galley of type and scrambled it to make a type specimen book. It has survived not only five centuries.</p>
  <div class="abs cta">CONTACT ME <svg viewBox="0 0 9 10"><path d="M0 0L9 5L0 10Z" fill="#fff"/></svg></div>
  <div class="abs dots"><i></i><i class="on"></i><i></i></div>
</section>

<section>
  <h2 class="abs section-title">SOLUTIONS FOR ALL YOUR ELECTRICAL REQUIREMENTS:</h2>
  <div class="abs service" style="left:122px;top:484px"><div class="thumb" role="img" aria-label="Recessed ceiling light" style="background:linear-gradient(#f4f4f4,#dcdcdc)"></div><p>Licht (house / office / outdoor)</p></div>
  <div class="abs service" style="left:394px;top:484px"><div class="thumb" role="img" aria-label="Outdoor wall lamp beside plants" style="background:linear-gradient(120deg,#8a9a5a,#d8d8cc 55%,#a89a62)"></div><p>Aussenbeleuchtung</p></div>
  <div class="abs service" style="left:664px;top:484px"><div class="thumb" role="img" aria-label="Network cabinet with cabling" style="background:linear-gradient(120deg,#9a9a9a,#2a2e30 45%,#3c4448)"></div><p>EDV / ADSL</p></div>
  <div class="abs service" style="left:122px;top:697px"><div class="thumb" role="img" aria-label="Distribution board with circuit breakers" style="background:linear-gradient(90deg,#8a4a20,#c7a48c 15%,#d2b09c)"></div><p>Steuerung</p></div>
  <div class="abs service" style="left:394px;top:697px"><div class="thumb" role="img" aria-label="Wall-mounted telephone unit" style="background:linear-gradient(90deg,#bcbcbc,#f2f2f2 40%,#cfcfcf)"></div><p>Telefonanlage</p></div>
  <div class="abs service" style="left:664px;top:697px"><div class="thumb" role="img" aria-label="Door bell intercom panel" style="background:linear-gradient(#e6e6e6,#cfcfcf)"></div><p>Sonnerie</p></div>
</section>

<section>
  <div class="abs divider"></div>
  <h3 class="abs col-title" style="left:122px">NEWS/RSS</h3>
  <h3 class="abs col-title" style="left:393px">TESTIMONIALS</h3>
  <h3 class="abs col-title" style="left:663px">MEET OUR TEAM</h3>
  <div class="abs news">
    <h4>Jan.13.2012</h4>
    <p>Lorem Ipsum is simply dummy text of the printing and typesetting industry. Lorem Ipsum has been the industry's standard dummy text ever since the 1500s.</p>
    <h4>Feb.18.2012</h4>
    <p>Lorem Ipsum is simply dummy text of the printing and typesetting industry. Lorem Ipsum has been the industry's standard dummy text ever since the 1500s.</p>
  </div>
  <div class="abs quote">
    <p>Lorem Ipsum is simply dummy text of the printing and typesetting industry. Lorem Ipsum has been the industry's standard dummy text ever since the 1500s, when an unknown printer took a galley of type and scrambled it to make a type specimen book. It has survived not only five centuries, but also the leap into electronic typesetting, remaining.</p>
    <p class="who">Mr. Lorem Ipsum</p>
    <a href="#">View All Testimonials</a>
  </div>
  <div class="abs team">
    <div role="img" aria-label="Team member portrait"></div>
    <div role="img" aria-label="Team member portrait"></div>
    <div role="img" aria-label="Team member portrait" style="background:linear-gradient(#7f8a4a,#d8b49a)"></div>
    <div role="img" aria-label="Team member portrait"></div>
    <div role="img" aria-label="Team member portrait" style="background:linear-gradient(#555,#3a3030)"></div>
    <div role="img" aria-label="Team member portrait" style="background:linear-gradient(#f2f2f2,#d9b0a0)"></div>
  </div>
</section>

<footer class="abs footer">
  <div class="line"><b>Brunner + Team</b> <span class="nm">Elektro AG</span> &nbsp;© 2012. All Rights Reserved &nbsp;| &nbsp;Privacy Policy</div>
  <span class="social" style="left:849px" aria-label="Social profile"></span>
  <span class="social" style="left:889px" aria-label="Social profile"></span>
</footer>
</body>
</html>
```